Business Card Design for BrightlaneReach.com

--I need a business card design for my company BrightlaneReach.com

I have attached my logo...I want the brightlane reach logo on the front of the business card, and then I want The Brightlane Chief on the back of it with my information.

I would like to see a light colored background as well as a dark colored background

FRONT:
BRIGHTLANE REACH LOGO
247 E. Pelham Row
5th Floor
San Diego CA 92384
www.BrightlaneReach.com

Advanced Website & App Development
Websites, Apps, Online Voucher Systems

Leading Edge Marketing Services
SMS, VB, SMM, SEM,

BACK:
BRIGHTLANE CHIEF LOGO
Dorian Welker
The Brightlane Chief
Call Or Text: 555-204-3378
Dorian@BrightlaneChief.com
www.BrightlaneChief.com

Target Market(s)

small business owners

Industry/Entity Type

Business Consultant

Contact Information for Business Card

FRONT:
BRIGHTLANE REACH LOGO
247 E. Pelham Row
5th Floor
San Diego CA 92384
www.BrightlaneReach.com

SMS, VB, SMM, SEM,

BACK:
BRIGHTLANE CHIEF LOGO
Dorian Welker
The Brightlane Chief
Dorian@BrightlaneChief.com
www.BrightlaneChief.com

Requirements
Must have
• add this quote on it somewhere, anywhere,preferrably on back
• "The Fastest Way To Success Is To Take Action”
• — Dorian Welker, Brightlane Chief
Nice to have
• open
Should not have
• red

```html
<!DOCTYPE html>
<html lang="en">
<head>
<meta charset="utf-8">
<title>Brightlane Reach Business Cards</title>
<link href="https://fonts.googleapis.com/css2?family=Montserrat:wght@400;500;600&family=Michroma&display=swap" rel="stylesheet">
<style>
  :root {
    --page-bg: #2b2b2d;
    --card-bg: #050505;
    --brand-blue: #1b7fc4;
    --text-white: #f2f2f2;
    --muted-grey: #8a8a8a;
  }
  * { margin: 0; padding: 0; box-sizing: border-box; }
  html, body {
    width: 1200px; height: 900px; overflow: hidden;
    background: var(--page-bg);
    font-family: "Montserrat", sans-serif;
    color: var(--text-white);
  }
  .canvas { position: relative; width: 1200px; height: 900px; }
  .card {
    position: absolute;
    width: 660px; height: 377px;
    background: var(--card-bg);
    border-radius: 22px;
    overflow: hidden;
    box-shadow: 0 18px 40px rgba(0,0,0,0.55);
  }
  .card--front { left: 90px; top: 50px; }
  .card--back { left: 450px; top: 473px; }

  /* Front */
  .brand-name {
    position: absolute; left: 0; right: 0; top: 58px;
    text-align: center;
    font-weight: 500; font-size: 42px; letter-spacing: 6px;
    color: var(--brand-blue);
  }
  .front-details {
    position: absolute; left: 0; right: 0; top: 140px;
    text-align: center; font-size: 15px; line-height: 20px;
  }
  .front-details .gap { height: 12px; }
  .blue { color: var(--brand-blue); }
  .services-highlight {
    color: var(--brand-blue); font-weight: 500; text-transform: uppercase; letter-spacing: 0.5px;
  }

  /* Back */
  .accent-bar {
    position: absolute; left: 0; top: 104px;
    width: 22px; height: 118px;
    background: var(--brand-blue);
    border-radius: 0 4px 4px 0;
  }
  .person { position: absolute; left: 44px; top: 94px; }
  .person-name { font-weight: 600; font-size: 24px; line-height: 30px; color: var(--brand-blue); }
  .person-title { font-size: 15px; line-height: 20px; margin-bottom: 8px; }
  .contact-list { list-style: none; font-size: 16px; line-height: 23px; }
  .contact-list li { display: flex; align-items: center; gap: 9px; }
  .contact-list svg { width: 12px; height: 12px; flex: none; }
  .chief-name {
    position: absolute; right: 36px; top: 248px;
    font-weight: 500; font-size: 28px; line-height: 34px; letter-spacing: 3px;
    color: var(--brand-blue);
    white-space: nowrap;
  }
  .tagline {
    position: absolute; right: 36px; bottom: 34px;
    font-family: "Michroma", sans-serif; font-size: 14px;
    letter-spacing: 0.3px; text-transform: uppercase;
    color: var(--text-white);
    white-space: nowrap;
  }
</style>
</head>
<body>
<main class="canvas">

  <section class="card card--front">
    <div class="brand-name">BRIGHTLANE REACH</div>
    <div class="front-details">
      <p>247 E. Pelham Row</p>
      <p>5th Floor</p>
      <p>San Diego CA 92384</p>
      <p>www.<span class="blue">BrightlaneReach</span>.com</p>
      <div class="gap"></div>
      <p>Advanced Website &amp; App Development</p>
      <p>Websites, Apps, Online Voucher Systems</p>
      <div class="gap"></div>
      <p class="services-highlight">Leading Edge Marketing Services</p>
      <p class="services-highlight">SMS, VB, SMM, SEM,</p>
    </div>
  </section>

  <section class="card card--back">
    <div class="accent-bar"></div>
    <div class="person">
      <p class="person-name">Dorian Welker</p>
      <p class="person-title">CEO</p>
      <ul class="contact-list">
        <li>
          <svg viewBox="0 0 12 12" aria-hidden="true"><path d="M2.5 1 L4.5 1 L5 3.5 L3.8 4.4 Q5 7 7.6 8.2 L8.5 7 L11 7.5 L11 9.5 Q11 11 9.5 11 Q1 10 1 2.5 Q1 1 2.5 1Z" fill="var(--brand-blue)"/></svg>
          <span>555-204-3378</span>
        </li>
        <li>
          <svg viewBox="0 0 12 12" aria-hidden="true"><rect x="1" y="2.5" width="10" height="7" fill="none" stroke="var(--brand-blue)" stroke-width="1.3"/><path d="M1 2.5 L6 6.5 L11 2.5" fill="none" stroke="var(--brand-blue)" stroke-width="1.3"/></svg>
          <span>Dorian@BrightlaneChief.com</span>
        </li>
        <li>
          <svg viewBox="0 0 12 12" aria-hidden="true"><circle cx="6" cy="6" r="5" fill="none" stroke="var(--brand-blue)" stroke-width="1.2"/><ellipse cx="6" cy="6" rx="2.2" ry="5" fill="none" stroke="var(--brand-blue)" stroke-width="1"/><line x1="1" y1="6" x2="11" y2="6" stroke="var(--brand-blue)" stroke-width="1"/></svg>
          <span>www.<span class="blue">BrightlaneChief</span>.com</span>
        </li>
      </ul>
    </div>
    <div class="chief-name">BRIGHTLANE CHIEF</div>
    <p class="tagline">The Fastest Way To Success Is To Take Action</p>
  </section>

</main>
</body>
</html>
```